Nine Rung Ledger Remedy Seminar

I would like a flyer to hand out to participants at the speeches that we give. We are a CPA firm that specializes in entrepreneurs and realtors. We would like a flyer that looks crisp and clean, that integrates our logo and our company colors (shades of blue & gold). We would like the wording to be as laid out in the attached documents, but design is up to you. We would like a picture to go along with each point and are open to ideas. The flyer should be one page, preferably just the front.

Colors
3176b5
fee18a

Requirements
Must have
• Our logo and the wording supplied.
• A picture to go along with each topic.
Nice to have
• Images that pop, clean look, professional.
Should not have
• Look messy.

```html
<!DOCTYPE html>
<html lang="en">
<head>
<meta charset="utf-8">
<title>Nine Rung Ledger Remedy Seminar Agenda</title>
<link href="https://fonts.googleapis.com/css2?family=Titillium+Web:ital,wght@0,400;0,600;0,700;0,900;1,600&family=Arimo:wght@400&display=swap" rel="stylesheet">
<style>
  :root{
    --brand-blue:#2c5ba6;
    --ring-blue:#5a8fd0;
    --line-blue:#9db9e0;
    --ink:#1d1d1d;
    --muted-gray:#8a8a8a;
    --gold:#c9a233;
    --paper:#f7f7f7;
  }
  *{margin:0;padding:0;box-sizing:border-box}
  html,body{width:894px;height:1200px;overflow:hidden;background:var(--paper)}
  .flyer{position:relative;width:894px;height:1200px;background:var(--paper);font-family:"Arimo",Arial,sans-serif;color:var(--ink)}
  .brand{position:absolute;left:65px;top:60px;width:240px}
  .brand-name{display:flex;align-items:center;gap:10px;font-family:"Titillium Web",sans-serif;font-weight:900;font-size:44px;line-height:1;color:var(--brand-blue)}
  .brand-name .mark{width:22px;height:22px;background:var(--gold);flex:none}
  .brand-tag{margin-top:14px;font-family:Georgia,serif;font-style:italic;font-weight:700;font-size:12.5px;color:var(--ink)}
  .headline{position:absolute;right:52px;top:40px;text-align:right;font-family:"Titillium Web",sans-serif;line-height:.95;text-transform:uppercase}
  .headline .lead{font-weight:900;font-size:62px;color:var(--brand-blue)}
  .headline .sub{font-weight:600;font-size:43px;color:var(--brand-blue);border-bottom:2px solid var(--muted-gray);padding-bottom:4px;margin-bottom:6px}
  .headline .gray{font-weight:900;font-size:42px;color:var(--muted-gray)}
  .path{position:absolute;left:0;top:0}
  .step{position:absolute;font-size:14.3px;line-height:1.22;text-align:justify}
  .step.left{left:65px;width:235px}
  .step.right{left:587px;width:250px}
  .step-num{display:flex;align-items:center;justify-content:center;gap:8px;margin-bottom:14px}
  .step-num::before,.step-num::after{content:"";width:40px;height:1.5px;background:var(--line-blue)}
  .step-num span{width:27px;height:27px;border-radius:50%;background:var(--ring-blue);color:#fff;font-family:"Titillium Web",sans-serif;font-weight:700;font-size:19px;display:flex;align-items:center;justify-content:center}
  .motto{position:absolute;left:470px;top:1010px;width:366px;font-family:"Titillium Web",sans-serif;font-style:italic;font-weight:600;font-size:24px;line-height:1.2;color:var(--ink)}
  .footer-band{position:absolute;left:0;top:1087px;width:894px;height:80px;background:var(--brand-blue);color:#fff;text-align:center;font-family:"Titillium Web",sans-serif}
  .footer-band .firm{font-size:17.5px;font-weight:600;margin-top:8px}
  .footer-band .addr{font-size:13.5px;margin-top:1px}
  .footer-band .phones{font-size:12.5px;margin-top:3px;display:flex;justify-content:center;gap:22px}
  .contact-row{position:absolute;left:0;top:1174px;width:894px;display:flex;justify-content:center;gap:20px;font-family:"Titillium Web",sans-serif;font-size:11.5px;color:var(--brand-blue)}
  .contact-row span::before{content:"";display:inline-block;width:9px;height:6px;background:var(--brand-blue);margin-right:4px;vertical-align:1px}
</style>
</head>
<body>
<div class="flyer">

  <div class="brand">
    <div class="brand-name"><span class="mark"></span>Tallyfield</div>
    <div class="brand-tag">A Professional Accounting Corporation</div>
  </div>

  <div class="headline">
    <div class="lead">Nine Rung</div>
    <div class="sub">Ledger Remedy</div>
    <div class="gray">Seminar</div>
    <div class="gray">Agenda</div>
  </div>

  <svg class="path" width="894" height="1200" viewBox="0 0 894 1200">
    <g fill="none" stroke="#5a8fd0" stroke-width="3.5">
      <path d="M425 296 C520 296 520 395 460 395 L400 395 C330 395 330 489 400 489 L456 489"/>
      <path d="M487 525 C470 560 450 583 425 583"/>
      <path d="M390 635 C400 670 430 681 456 681"/>
      <path d="M487 727 C470 755 450 768 425 768"/>
      <path d="M390 820 C400 855 430 868 456 868"/>
      <path d="M487 914 C470 942 450 954 425 954"/>
      <circle cx="369" cy="296" r="55" fill="#fff"/>
      <circle cx="512" cy="489" r="55" fill="#fff"/>
      <circle cx="369" cy="583" r="55" fill="#fff"/>
      <circle cx="512" cy="681" r="55" fill="#fff"/>
      <circle cx="369" cy="768" r="55" fill="#fff"/>
      <circle cx="512" cy="868" r="55" fill="#fff"/>
      <circle cx="369" cy="954" r="55" fill="#fff"/>
    </g>
    <!-- step icons -->
    <g fill="#111">
      <rect x="342" y="277" width="40" height="36" fill="none" stroke="#111" stroke-width="2.5" stroke-dasharray="6 4"/>
      <circle cx="362" cy="295" r="11"/>
      <text x="362" y="300" fill="#fff" font-family="Arial,sans-serif" font-weight="700" font-size="14" text-anchor="middle">$</text>
      <path d="M386 285 L398 308 M398 285 L386 308" stroke="#111" stroke-width="2.2" fill="none"/>
      <path d="M492 486 L512 468 L532 486 Z" fill="none" stroke="#111" stroke-width="3"/>
      <rect x="498" y="485" width="28" height="20" fill="none" stroke="#111" stroke-width="3"/>
      <text x="512" y="501" font-family="Arial,sans-serif" font-weight="700" font-size="15" text-anchor="middle">$</text>
      <circle cx="364" cy="576" r="14" fill="none" stroke="#111" stroke-width="3.5"/>
      <path d="M374 587 L390 603" stroke="#111" stroke-width="6" stroke-linecap="round"/>
      <path d="M358 576 L363 581 L371 571" stroke="#111" stroke-width="2.5" fill="none"/>
      <rect x="488" y="660" width="48" height="44" rx="6" fill="#111" role="img" aria-label="Icon of a client and advisor meeting with approval tick"/>
      <path d="M502 678 L510 686 L523 671" stroke="#fff" stroke-width="3.5" fill="none"/>
      <rect x="346" y="746" width="46" height="44" rx="6" fill="#111" role="img" aria-label="Icon of a family with savings jar"/>
      <rect x="490" y="846" width="44" height="44" rx="6" fill="#111" role="img" aria-label="Icon of a graduate in cap and gown"/>
      <rect x="344" y="958" width="7" height="16"/><rect x="355" y="951" width="7" height="23"/>
      <rect x="366" y="945" width="7" height="29"/><rect x="377" y="938" width="7" height="36"/>
      <path d="M342 952 L360 936 L372 944 L392 926" stroke="#111" stroke-width="4" fill="none"/>
      <path d="M384 924 L396 922 L394 934 Z"/>
    </g>
  </svg>

  <div class="step left" style="top:208px">
    <div class="step-num"><span>1</span></div>
    We will first show you how to eliminate much of your self-employment tax on your return by converting your business into an S Corporation. A business owner making over $120,000 per year can save about $12,000 per year by doing this.
  </div>

  <div class="step right" style="top:382px">
    <div class="step-num"><span>2</span></div>
    We will show you how to get tax free income from your corporation by renting you home to the corporation for the board meetings. Many of our clients are getting up to $21,000 in tax free income which could put $8,400 cash into your pocket.
  </div>

  <div class="step left" style="top:476px">
    <div class="step-num"><span>3</span></div>
    We will show you the easiest way to track your expenses so that the only thing you will have to do to have rock solid books is to take a picture of the receipt and throw it away. It doesn't get any better than that.
  </div>

  <div class="step right" style="top:590px">
    <div class="step-num"><span>4</span></div>
    Next, we show you the importance of tax planning and why it is critical to meet with your CPA before the end of the year and not just when you do your tax preparation.
  </div>

  <div class="step left" style="top:687px">
    <div class="step-num"><span>5</span></div>
    We will show you how to hire your children and get $7,500 per child tax free. This will save you $3,000 per child in income tax reduction.
  </div>

  <div class="step right" style="top:775px">
    <div class="step-num"><span>6</span></div>
    We will discuss how to make your child's college education tax deductible. With college cost spiraling out of control this is a biggie. Most of our clients have a savings of about $12,000 per year of college.
  </div>

  <div class="step left" style="top:851px">
    <div class="step-num"><span>7</span></div>
    Our grand finale is to show you how to use, not one, but two corporations to get a several hundred thousand dollar tax deferral, get an interest free loan from the government and use that money to grow your business and your wealth.
  </div>

  <p class="motto">If they drive by with a machine gun you don't have to stand up.</p>

  <div class="footer-band">
    <div class="firm">TALLYFIELD PARTNERS, A Professional Accounting Corporation</div>
    <div class="addr">2870 N. Orchard Ave, Ste. B, Lindale, CA 95412</div>
    <div class="phones"><span>&#9742; 555-014-2271</span><span>&#9113; 555-014-2290</span></div>
  </div>

  <div class="contact-row">
    <span>dana@tallyfieldcpas.com</span>
    <span>owen@tallyfieldcpas.com</span>
    <span>www.tallyfieldcpa.com</span>
  </div>
</div>
</body>
</html>
```